Quillmore Website design

Create a sophisticated minimalist shopify ecommerce store that can be integrated with stockwise hub POS.

Quillmore is a Brick and mortar store that is focused on exceptional customer service and quality Ladies fashion and specialty swimwear for Women, Men and Children.

This website will need to be easy to navigate by the end user and manage inhouse.

With so many different product categories and customer demographics it will be difficult to make seamless and easy to navigate.

Think The Varnel, Lumo etc where there are Women, Men and Kids

It would be fantastic to build a site with three different navigations to constant themes that are modified to suit each demographic.

We have a logo to use and would like the theme to be easily updated as seasons change and our business evolves.

The website must be set up to use SEO for google and other leading search engines.

Stock will be supplied from either our brick and mortar store or warehouse so would need to consist of multiple store locations as far as the back end is concerned.

It will need to be set up with apps that allow us to stream line our fullfilment in house (label printing, picking lists and shipping with Kestrel Freight)

```html
<!DOCTYPE html>
<html lang="en">
<head>
<meta charset="utf-8">
<title>Quillmore — Fashion &amp; Swimwear</title>
<link rel="stylesheet" href="https://fonts.googleapis.com/css2?family=Poppins:wght@300;400;500;600;700&family=DM+Serif+Display&display=swap">
<style>
:root{
  --sage:#6e7d5c;
  --sage-dark:#5f6d4f;
  --ink:#1f1f1f;
  --muted:#5a5a5a;
  --line:#d9d9d9;
  --tile:#efefef;
  --hero:#e9e9e9;
  --red:#b8473b;
  --white:#ffffff;
}
*{box-sizing:border-box;margin:0;padding:0}
html,body{width:1200px;height:4728px;overflow:hidden}
body{position:relative;font-family:'Poppins',sans-serif;color:var(--ink);background:var(--white)}
.abs{position:absolute}
.ph{position:absolute;overflow:hidden}

/* top bar & header */
.utility{left:0;top:0;width:1200px;height:24px;background:var(--sage-dark);color:#e8ecdf;font-size:8.5px;display:flex;gap:22px;align-items:center;padding-left:125px}
.utility span::before{content:"";display:inline-block;width:7px;height:7px;border:1px solid #e8ecdf;border-radius:2px;margin-right:4px;vertical-align:-1px}
.header{left:0;top:24px;width:1200px;height:114px;background:var(--sage)}
.logo{position:absolute;left:120px;top:26px;width:118px;text-align:center;color:var(--white);font-weight:300;font-size:19px;letter-spacing:3px}
.logo .mark{display:block;width:26px;height:26px;border:1.5px solid var(--white);border-radius:50%;margin:0 auto 8px}
.main-nav{position:absolute;left:363px;top:33px;display:flex;gap:0;font-size:9px;font-weight:600;color:var(--white);letter-spacing:.3px}
.main-nav span{width:60px}
.sub-nav{position:absolute;left:362px;top:89px;display:flex;gap:28px;font-size:7.5px;color:#eef1e8;letter-spacing:.3px}
.sale{position:absolute;right:125px;top:88px;font-size:9px;font-weight:600;color:var(--white)}
.search{position:absolute;left:719px;top:24px;width:221px;height:30px;background:var(--white);border-radius:2px;font-size:8px;color:#999;padding:9px 12px}
.search svg{position:absolute;right:10px;top:9px}
.icons{position:absolute;left:986px;top:27px;display:flex;gap:17px}

.benefits{left:0;top:150px;width:1200px;display:flex;justify-content:center;gap:44px;font-size:8.5px;font-weight:600}
.benefits span{display:flex;align-items:center;gap:6px}

/* hero */
.hero{left:125px;top:183px;width:950px;height:443px;background:var(--hero)}
.hero h2{position:absolute;left:68px;top:116px;font-weight:400;font-size:29px;letter-spacing:-.5px}
.hero h1{position:absolute;left:66px;top:146px;font-weight:600;font-size:70px;letter-spacing:-2.5px;line-height:1}
.hero p{position:absolute;left:70px;top:245px;width:300px;font-size:11px;line-height:16px;color:#444}
.btn-outline{position:absolute;border:1.5px solid var(--ink);font-size:8px;font-weight:600;display:flex;align-items:center;justify-content:center;letter-spacing:.2px}

/* promos */
.promo{top:688px;width:469px;height:468px}
.promo-title{position:absolute;width:100%;text-align:center;font-family:'DM Serif Display',serif;color:var(--white)}
.demo{top:1218px;height:366px}
.demo-label{position:absolute;left:26px;top:24px;font-family:'DM Serif Display',serif;font-size:31px;color:var(--white)}
.demo-band{position:absolute;left:0;bottom:0;width:100%;height:24px;color:var(--white);font-size:12px;font-weight:600;letter-spacing:2.6px;display:flex;align-items:center;justify-content:center}

/* new season */
.season{left:125px;top:1659px;width:950px;height:429px;background:#e6e6e6}
.season h2{position:absolute;left:75px;top:98px;font-weight:600;font-size:50px;letter-spacing:-1.5px;line-height:56px}
.season h2 em{font-style:normal;color:var(--sage)}
.season p{position:absolute;left:78px;top:234px;font-size:14px}

/* section heading */
.sec-h{left:125px;font-size:19px;font-weight:600;letter-spacing:-.3px}
.arrows{display:flex;gap:9px}
.arrows i{width:20px;height:20px;display:flex;align-items:center;justify-content:center;background:#e4e4e4;color:#777;font-style:normal;font-size:10px}
.arrows i.next{background:var(--sage);color:var(--white)}
.label{font-size:11px;font-weight:600}
.row{display:flex;position:absolute;left:125px;width:950px}

.fav{width:150px;margin-right:10px}
.fav:last-child{margin-right:0}
.fav .img{height:168px;background:var(--tile)}
.fav .label{margin-top:14px}

.latest{width:309px;margin-right:11px}
.latest:last-child{margin-right:0}
.latest .img{height:339px}
.latest h4{font-size:11px;font-weight:600;margin-top:19px}
.latest p{font-size:9.5px;line-height:16px;color:#555;margin-top:8px;width:290px}

.cta{position:absolute;top:2980px;height:50px;color:var(--white);font-size:10px;font-weight:600;display:flex;align-items:center;justify-content:center;letter-spacing:.2px}
.cta svg{position:absolute;right:22px;top:19px}

.cat{width:229px;margin-right:11px}
.cat:last-child{margin-right:0}
.cat .img{height:228px}
.cat .label{margin-top:17px}

.brand{width:150px;height:135px;margin-right:10px;background:var(--tile);display:flex;align-items:center;justify-content:center;font-size:17px;font-weight:600;letter-spacing:-.3px;text-align:center;line-height:1.1}
.brand:last-child{margin-right:0}

/* seo */
.seo{left:125px;top:3690px;width:950px}
.seo h3{font-size:19px;font-weight:600;letter-spacing:-.3px}
.seo .lead{font-size:10px;line-height:17px;color:#555;margin-top:12px}
.seo dl{margin-top:26px}
.seo .item{display:flex;height:55.6px}
.seo dt{width:67px;font-size:11px;font-weight:600;padding-top:6px}
.seo dd{width:860px;font-size:10px;line-height:17px;color:#555}

/* footer */
.footer{left:0;top:4165px;width:1200px;height:563px;background:var(--sage);color:var(--white)}
.fcol{position:absolute;top:58px}
.fcol h5{font-size:9px;font-weight:600;margin-bottom:13px}
.fcol li{list-style:none;font-size:8.3px;line-height:13.8px;color:#eef1e8}
.social li{display:flex;align-items:center;gap:6px}
.social li::before{content:"";width:7px;height:7px;border:1px solid #eef1e8;border-radius:50%}
.news-row{display:flex;margin-top:16px;height:32px}
.news-row .sel{width:73px;background:var(--white);color:var(--ink);font-size:8px;padding:10px 12px}
.news-row .inp{width:155px;background:var(--white);border-left:1px solid var(--line);color:#999;font-size:8px;padding:10px 10px}
.news-row .sub{width:73px;margin-left:7px;background:var(--white);color:var(--ink);font-size:9px;font-weight:600;display:flex;align-items:center;justify-content:center}
.chat{left:1105px;top:4408px;width:66px;height:66px;border-radius:50%;background:#8a9878;display:flex;align-items:center;justify-content:center}
.top-searches{position:absolute;left:125px;top:310px;font-size:9px;font-weight:600}
.ts-col{position:absolute;top:340px;font-size:8.3px;line-height:13.8px;color:#eef1e8;list-style:none}
.copy{position:absolute;left:125px;top:482px;font-size:8.5px;font-weight:500}
.flogo{position:absolute;left:530px;top:445px;width:140px;text-align:center;font-weight:300;font-size:19px;letter-spacing:3px}
.flogo .mark{display:block;width:26px;height:26px;border:1.5px solid var(--white);border-radius:50%;margin:0 auto 8px}
.badge{position:absolute;top:468px;width:119px;height:41px;background:var(--white);border-radius:5px}
</style>
</head>
<body>

<div class="abs utility">
  <span>Contact &amp; FAQs</span><span>Delivery</span><span>Returns</span><span>Track Orders</span><span>Share Your Ideas</span><span>Gift Cards</span>
</div>

<header class="abs header">
  <div class="logo"><span class="mark"></span>QUILLMORE</div>
  <nav class="main-nav"><span>HOME</span><span>WOMEN</span><span>MEN</span><span>KIDS</span><span>SHORT</span><span>BEAUTY</span></nav>
  <div class="search">Search for products, brands...
    <svg width="11" height="11" viewBox="0 0 11 11" fill="none" stroke="#333" stroke-width="1.3"><circle cx="4.5" cy="4.5" r="3.5"/><path d="M7 7l3 3"/></svg>
  </div>
  <div class="icons">
    <svg width="18" height="18" viewBox="0 0 18 18" fill="none" stroke="#fff" stroke-width="1.3"><circle cx="9" cy="6" r="3.5"/><path d="M2.5 16.5c1-3.5 3.5-5 6.5-5s5.5 1.5 6.5 5"/></svg>
    <svg width="18" height="18" viewBox="0 0 18 18" fill="none" stroke="#fff" stroke-width="1.3"><path d="M9 15.5S2 11.5 2 6.5A3.5 3.5 0 0 1 9 5a3.5 3.5 0 0 1 7 1.5c0 5-7 9-7 9z"/></svg>
    <svg width="18" height="18" viewBox="0 0 18 18" fill="none" stroke="#fff" stroke-width="1.3"><path d="M1.5 2.5h2.5l2 9h8.5l1.5-6.5H5"/><circle cx="7" cy="15" r="1.2"/><circle cx="13.5" cy="15" r="1.2"/></svg>
  </div>
  <nav class="sub-nav"><span>NEW IN</span><span>CLOTHING</span><span>SHOES</span><span>ACCESSORIES</span><span>SPORT</span><span>BRANDS</span><span>DESIGNER</span><span>SNEAKERHUB</span></nav>
  <div class="sale">SALE</div>
</header>

<div class="abs benefits">
  <span><svg width="16" height="12" viewBox="0 0 16 12" fill="none" stroke="#333" stroke-width="1.1"><path d="M1 1.5h9v7H1zM10 4h3l2 2.5v2h-5"/><circle cx="4" cy="10" r="1.3"/><circle cx="12" cy="10" r="1.3"/></svg>FREE SHIPPING</span>
  <span><svg width="14" height="14" viewBox="0 0 14 14" fill="none" stroke="#333" stroke-width="1.1"><circle cx="7" cy="7.5" r="5.5"/><path d="M7 4.5v3l2 1.5M5.5 1h3"/></svg>FAST DELIVERY</span>
  <span><svg width="16" height="14" viewBox="0 0 16 14" fill="none" stroke="#333" stroke-width="1.1"><path d="M2 3h9v9H2zM5 3V1h9v9h-3"/></svg>FREE RETURNS</span>
</div>

<section class="abs hero">
  <div class="ph" style="left:420px;top:0;width:530px;height:443px;background:linear-gradient(100deg,#e9e9e9 0%,#c9a59a 30%,#e6c4c0 60%,#d7dbe6 85%,#ececec 100%)" role="img" aria-label="Two models in casual layered outfits, one in a red checked shirt, one in a pink cardigan"></div>
  <h2>Effortless Elegance,</h2>
  <h1>Everyday.</h1>
  <p>Discover timeless styles and statement swimwear designed to flatter every season.</p>
  <div class="btn-outline" style="left:70px;top:296px;width:152px;height:33px">SHOP THE COLLECTION</div>
</section>

<section class="abs promo" style="left:125px">
  <div class="ph" style="inset:0;background:linear-gradient(180deg,#8aa4b4 0%,#b7a99a 30%,#9f8b7b 65%,#8f7f72 100%)" role="img" aria-label="Woman in a swimsuit on the beach with arms raised above her head"></div>
  <div class="promo-title" style="top:332px;font-size:46px;letter-spacing:1px">SWIMWEAR</div>
  <div class="promo-title" style="top:392px;font-family:'Poppins',sans-serif;font-weight:600;font-size:17px;line-height:24px;letter-spacing:-.3px">SPEND $80, SAVE 20%<br>SPEND $100, SAVE 25%</div>
</section>

<section class="abs promo" style="left:606px">
  <div class="ph" style="inset:0;background:linear-gradient(180deg,#ececec 0%,#dcdcdc 100%)"></div>
  <div class="ph" style="left:140px;top:40px;width:200px;height:420px;background:linear-gradient(180deg,#6e5247 0%,#4a3a35 55%,#cfcfcf 100%);border-radius:40px 40px 6px 6px" role="img" aria-label="Couple in spring coats posing together"></div>
  <div class="abs" style="left:52px;top:58px;font-size:35px;font-weight:600;color:var(--white);letter-spacing:-1px">Spring</div>
  <div class="abs" style="left:328px;top:102px;font-size:35px;font-weight:600;color:var(--white);letter-spacing:-1px">Cloths</div>
  <div class="abs" style="left:350px;top:408px;font-size:12px;font-weight:500">SHOP NOW &nbsp;›</div>
</section>

<section class="abs ph demo" style="left:125px;width:310px">
  <div class="ph" style="inset:0;background:linear-gradient(160deg,#d9d2cb 0%,#a1584a 45%,#7a4a3a 75%,#c8c0b8 100%)" role="img" aria-label="Woman in a red polka dot top carrying a tan bag"></div>
  <div class="demo-label">Women’s</div>
  <div class="demo-band" style="background:var(--sage)">MID-SEASON SALE UP TO 50% OFF*</div>
</section>
<section class="abs ph demo" style="left:446px;width:308px">
  <div class="ph" style="inset:0;background:linear-gradient(160deg,#cfcac5 0%,#a37b58 45%,#e8e4df 70%,#b9b2ab 100%)" role="img" aria-label="Man in a camel coat over a white shirt"></div>
  <div class="demo-label">Men’s</div>
  <div class="demo-band" style="background:var(--red)">MID-SEASON SALE UP TO 50% OFF*</div>
</section>
<section class="abs ph demo" style="left:765px;width:310px">
  <div class="ph" style="inset:0;background:linear-gradient(160deg,#a57a56 0%,#d8b995 40%,#e1ccb5 70%,#c7a78a 100%)" role="img" aria-label="Young girl in sunglasses wearing a denim vest"></div>
  <div class="demo-label">Kid’s</div>
  <div class="demo-band" style="background:#2b2b2b">MID-SEASON SALE UP TO 50% OFF*</div>
</section>

<section class="abs season">
  <div class="ph" style="left:410px;top:0;width:540px;height:429px;background:linear-gradient(90deg,#e6e6e6 0%,#2c3a66 22%,#1e1e1e 48%,#4d5b3e 70%,#b9aa97 88%,#e0e0e0 100%)" role="img" aria-label="Woman in black holding a navy jumper beside a clothing rail and mirror"></div>
  <h2>New Season.<br><em>New Styles</em></h2>
  <p>Update your wardrobe with our latest arrivals.</p>
  <div class="btn-outline" style="left:79px;top:277px;width:152px;height:33px">SHOP THE COLLECTION</div>
</section>

<!-- favourites -->
<div class="abs sec-h" style="top:2147px">Shop Your Favourites</div>
<div class="abs arrows" style="left:1022px;top:2153px"><i>‹</i><i class="next">›</i></div>
<div class="row" style="top:2195px">
  <div class="fav"><div class="img" role="img" aria-label="Model in a grey shirt dress" style="background:linear-gradient(180deg,#f0f0f0,#8e929a 60%,#e9e9e9)"></div><div class="label">Dresses</div></div>
  <div class="fav"><div class="img" role="img" aria-label="Model in a pink puffer jacket" style="background:linear-gradient(180deg,#f0f0f0,#d9a9ab 50%,#7d8aa6 85%)"></div><div class="label">Coats &amp; Jackets</div></div>
  <div class="fav"><div class="img" role="img" aria-label="Model in a grey knit jumper" style="background:linear-gradient(180deg,#f0f0f0,#8b8b8b 55%,#dedede)"></div><div class="label">Knitwear</div></div>
  <div class="fav"><div class="img" role="img" aria-label="Model in a white top and blue jeans" style="background:linear-gradient(180deg,#f0f0f0,#f5f5f5 35%,#7f9ac0 70%,#eaeaea)"></div><div class="label">Jeans</div></div>
  <div class="fav"><div class="img" role="img" aria-label="Feet in cream flats with rolled jeans" style="background:linear-gradient(180deg,#9ab1cc,#d8c8b8 60%,#efefef)"></div><div class="label">Flats</div></div>
  <div class="fav"><div class="img" role="img" aria-label="Model in a sage green activewear set" style="background:linear-gradient(180deg,#f0f0f0,#93a69a 50%,#e8e8e8)"></div><div class="label">Activewear</div></div>
</div>

<!-- latest -->
<div class="abs sec-h" style="top:2443px">Shop The Latest</div>
<div class="abs arrows" style="left:1022px;top:2449px"><i>‹</i><i class="next">›</i></div>
<div class="row" style="top:2492px">
  <div class="latest"><div class="img" role="img" aria-label="Woman in a plaid coat and white skirt seated with a handbag" style="background:linear-gradient(170deg,#3a2e26 0%,#8a5a3c 35%,#e6e2dc 65%,#4b3a2f 100%)"></div>
    <h4>Desire: VELLA SS25</h4><p>Aenean sollicitudin lorem quis bibendum auctor, nisi elit consequat ipsum nec sagittis sem nibh id elit is duis sed odio sit amet nibh vulputate.</p></div>
  <div class="latest"><div class="img" role="img" aria-label="Skincare bottles arranged on stone plinths with a dried leaf" style="background:linear-gradient(180deg,#d8cbbd 0%,#e8ddd2 50%,#cdb9a6 100%)"></div>
    <h4>Spring Renewal</h4><p>Aenean sollicitudin lorem quis bibendum auctor, nisi elit consequat ipsum nec sagittis sem nibh id elit is duis sed odio sit amet nibh vulputate.</p></div>
  <div class="latest"><div class="img" role="img" aria-label="Man in a brown tracksuit seated on a white block" style="background:linear-gradient(180deg,#eeeeee 0%,#7a5e4b 45%,#6b5242 75%,#e4e4e4 100%)"></div>
    <h4>Spring into Motion</h4><p>Aenean sollicitudin lorem quis bibendum auctor, nisi elit consequat ipsum nec sagittis sem nibh id elit is duis sed odio sit amet nibh vulputate.</p></div>
</div>

<div class="cta" style="left:125px;width:464px;background:var(--sage)">NEW HERE? $20 OFF YOUR FIRST PURCHASE
  <svg width="14" height="12" viewBox="0 0 14 12" fill="none" stroke="#fff" stroke-width="1.3"><path d="M0 6h13M8 1l5 5-5 5"/></svg></div>
<div class="cta" style="left:607px;width:465px;background:#222">GET $20 CREDIT WHEN YOU REFER A FRIEND
  <svg width="14" height="12" viewBox="0 0 14 12" fill="none" stroke="#fff" stroke-width="1.3"><path d="M0 6h13M8 1l5 5-5 5"/></svg></div>

<!-- category -->
<div class="abs sec-h" style="top:3089px">Shop by Category</div>
<div class="abs arrows" style="left:1022px;top:3095px"><i>‹</i><i class="next">›</i></div>
<div class="row" style="top:3134px">
  <div class="cat"><div class="img" role="img" aria-label="Two people stretching outdoors in sportswear by the sea" style="background:linear-gradient(180deg,#c9c0b6 0%,#e3d2c0 45%,#5a5a5a 75%,#9a8f86 100%)"></div><div class="label">Sport</div></div>
  <div class="cat"><div class="img" role="img" aria-label="Hands holding beauty and skincare tubes" style="background:linear-gradient(180deg,#d7dee0 0%,#e9ded3 50%,#c8d8cf 100%)"></div><div class="label">Beauty</div></div>
  <div class="cat"><div class="img" role="img" aria-label="Woman seated with pink designer bags" style="background:linear-gradient(180deg,#b9bdd8 0%,#efe9e6 45%,#d96b70 75%,#c7c9dd 100%)"></div><div class="label">Women's Designer</div></div>
  <div class="cat"><div class="img" role="img" aria-label="Man in a white shirt seated beside timber panels" style="background:linear-gradient(90deg,#b37f55 0%,#d8a77c 20%,#e6e1dc 45%,#f1efed 100%)"></div><div class="label">Men's Designer</div></div>
</div>

<!-- brands -->
<div class="abs sec-h" style="top:3449px">Shop brands</div>
<div class="abs arrows" style="left:1022px;top:3455px"><i>‹</i><i class="next">›</i></div>
<div class="row" style="top:3498px">
  <div class="brand">Stridon</div>
  <div class="brand">Harlow<br>Fenwick</div>
  <div class="brand" style="background:linear-gradient(160deg,#3a4a66,#7a1f1f 60%,#2a2a2a);color:var(--white)" role="img" aria-label="Denim jeans with brand tag, Denholt">Denholt</div>
  <div class="brand">Maison Orvel</div>
  <div class="brand">Vantra</div>
  <div class="brand">Corra &amp; Vale</div>
</div>

<!-- seo copy -->
<section class="abs seo">
  <h3>Shop For The Latest Clothing, Shoes, Home &amp; Beauty Products</h3>
  <p class="lead">Delivering new arrivals from the biggest brands and exclusive labels, QUILLMORE is your go-to for clothing, footwear, sportswear, beauty, home and kidswear, established as Australia’s leading online fashion and lifestyle retailer.</p>
  <dl>
    <div class="item"><dt>Women</dt><dd>Delivering new arrivals from the biggest brands and exclusive labels, QUILLMORE is your go-to for clothing, footwear, sportswear, beauty, home and kidswear, established as Australia’s leading online fashion and lifestyle retailer.</dd></div>
    <div class="item"><dt>Men</dt><dd>Delivering new arrivals from the biggest brands and exclusive labels, QUILLMORE is your go-to for clothing, footwear, sportswear, beauty, home and kidswear, established as Australia’s leading online fashion and lifestyle retailer.</dd></div>
    <div class="item"><dt>Beauty</dt><dd>Delivering new arrivals from the biggest brands and exclusive labels, QUILLMORE is your go-to for clothing, footwear, sportswear, beauty, home and kidswear, established as Australia’s leading online fashion and lifestyle retailer.</dd></div>
    <div class="item"><dt>Sports</dt><dd>Delivering new arrivals from the biggest brands and exclusive labels, QUILLMORE is your go-to for clothing, footwear, sportswear, beauty, home and kidswear, established as Australia’s leading online fashion and lifestyle retailer.</dd></div>
    <div class="item"><dt>Home</dt><dd>Delivering new arrivals from the biggest brands and exclusive labels, QUILLMORE is your go-to for clothing, footwear, sportswear, beauty, home and kidswear, established as Australia’s leading online fashion and lifestyle retailer.</dd></div>
    <div class="item"><dt>Kids</dt><dd>Delivering new arrivals from the biggest brands and exclusive labels, QUILLMORE is your go-to for clothing, footwear, sportswear, beauty, home and kidswear, established as Australia’s leading online fashion and lifestyle retailer.</dd></div>
  </dl>
</section>

<footer class="abs footer">
  <div class="fcol" style="left:125px"><h5>QUILLMORE</h5><ul>
    <li>About Us</li><li>Acknowledgement Of Country</li><li>Affiliates</li><li>Brands</li><li>Partnerships</li><li>Influencers</li><li>Press</li><li>Careers</li><li>Terms &amp; Conditions</li><li>Promotions and Competitions</li><li>Privacy Policy</li><li>Online Security Advice</li></ul></div>
  <div class="fcol" style="left:323px"><h5>HELP &amp; SUPPORT</h5><ul>
    <li>FAQs &amp; Contact</li><li>Delivery</li><li>Returns</li><li>Size Guide</li><li>Gift Cards</li><li>Fashion Glossary</li><li>Product Ideas</li><li>Product Recall</li></ul></div>
  <div class="fcol social" style="left:477px"><h5>FOLLOW US</h5><ul>
    <li>Snapwall</li><li>Friendline</li><li>Chirper</li><li>Pinboard</li><li>Vidstream</li></ul></div>
  <div class="fcol" style="left:767px;width:308px"><h5>STAY IN TOUCH</h5>
    <div style="font-size:8.3px">Sign up to QUILLMORE News for your <b>$20 voucher.*</b></div>
    <div class="news-row"><div class="sel">Women &nbsp;&nbsp;⌄</div><div class="inp">Enter your email address</div><div class="sub">SUBMIT</div></div>
  </div>

  <div class="top-searches">OUR TOP SEARCHES</div>
  <ul class="ts-col" style="left:125px"><li>Denholt</li><li>Stridon</li><li>Bexley Row</li></ul>
  <ul class="ts-col" style="left:251px"><li>Corkwell</li><li>Corra</li><li>Meadow Lane</li><li>Shoes</li></ul>
  <ul class="ts-col" style="left:382px"><li>Canvaso</li><li>Aesopa</li><li>Skatewell</li><li>Evermore</li></ul>
  <ul class="ts-col" style="left:517px"><li>Wrenfield</li><li>Skincare</li><li>Packwright</li><li>Lisle &amp; Co</li></ul>
  <ul class="ts-col" style="left:635px"><li>Lunaactive</li><li>Trueform</li><li>Vantra</li><li>Swimwear</li></ul>
  <ul class="ts-col" style="left:752px"><li>Calder Kent</li><li>Ruby Rae</li><li>Pacera</li><li>Harlow Fenwick</li></ul>
  <ul class="ts-col" style="left:899px"><li>Sneakers</li><li>Sandals</li><li>Ascend</li><li>Dresses</li></ul>
  <ul class="ts-col" style="left:1015px"><li>Jeans</li><li>Tobin Hale</li><li>Toro Bellini</li><li>Pace Nation</li></ul>

  <div class="copy">© COPYRIGHT 2025 QUILLMORE ALL RIGHTS RESERVED</div>
  <div class="flogo"><span class="mark"></span>QUILLMORE</div>
  <div class="badge" style="left:826px"></div>
  <div class="badge" style="left:954px"></div>
</footer>

<div class="abs chat">
  <svg width="30" height="26" viewBox="0 0 30 26" fill="none"><path d="M4 2h22a2 2 0 0 1 2 2v13a2 2 0 0 1-2 2H12l-6 5v-5H4a2 2 0 0 1-2-2V4a2 2 0 0 1 2-2z" fill="#fff"/><circle cx="10" cy="10.5" r="1.6" fill="#8a9878"/><circle cx="15" cy="10.5" r="1.6" fill="#8a9878"/><circle cx="20" cy="10.5" r="1.6" fill="#8a9878"/></svg>
</div>

</body>
</html>
```